Birch Flooring Supply

Basic one-sided business card design using the attached logo. Vintage americana theme. Font is modified Arial Nova Cond, but anything that coordinates can be used

```html
<!DOCTYPE html>
<html lang="en">
<head>
<meta charset="utf-8">
<title>Birch Flooring Supply – Business Card</title>
<link href="https://fonts.googleapis.com/css2?family=Roboto+Condensed:wght@400;700&display=swap" rel="stylesheet">
<style>
  :root {
    --backdrop: #e4e4e4;
    --card-black: #07090c;
    --gold: #a88b64;
    --white: #ffffff;
    --pattern-grey: #d2d2d2;
    --text-soft: #eeeeee;
  }
  html, body {
    margin: 0;
    padding: 0;
    width: 1200px;
    height: 1200px;
    overflow: hidden;
    background: var(--backdrop);
    font-family: "Roboto Condensed", "Arial Narrow", sans-serif;
  }
  .canvas {
    position: relative;
    width: 1200px;
    height: 1200px;
  }
  .card {
    position: absolute;
    left: 152px;
    width: 914px;
    background: var(--card-black);
    overflow: hidden;
  }
  .card--front { top: 52px; height: 519px; }
  .card--back  { top: 626px; height: 523px; }

  .brand-seal {
    position: absolute;
    border-radius: 50%;
    box-sizing: border-box;
    display: flex;
    flex-direction: column;
    align-items: center;
    justify-content: center;
    text-align: center;
    color: var(--white);
    font-weight: 700;
  }
  .card--front .brand-seal {
    left: 305px; top: 108px;
    width: 304px; height: 304px;
    border: 4px solid var(--gold);
  }
  .card--back .brand-seal {
    left: 320px; top: 38px;
    width: 280px; height: 280px;
    background: var(--card-black);
    z-index: 2;
  }
  .brand-name {
    margin: 0;
    line-height: 1;
    font-weight: 700;
    color: var(--white);
  }
  .brand-name__main { display: block; font-size: 72px; letter-spacing: 1px; }
  .brand-name__sub  { display: block; font-size: 22px; letter-spacing: 2px; margin-top: 6px; }
  .card--back .brand-name__main { font-size: 64px; }
  .card--back .brand-name__sub  { font-size: 19px; }

  .pattern-band {
    position: absolute;
    left: 0; top: 0;
    width: 100%; height: 176px;
    background: linear-gradient(180deg, #e3e3e3, var(--pattern-grey));
  }
  .gold-rule {
    position: absolute;
    left: 0; top: 176px;
    width: 100%; height: 19px;
    background: var(--gold);
  }

  .contact-person {
    position: absolute;
    left: 258px; top: 338px;
    color: var(--text-soft);
  }
  .contact-person__name {
    margin: 0;
    font-size: 38px;
    font-weight: 400;
    line-height: 1.05;
  }
  .contact-person__role {
    margin: 2px 0 0 8px;
    font-size: 22px;
    font-weight: 400;
    letter-spacing: 0.5px;
  }
  .divider {
    position: absolute;
    left: 458px; top: 340px;
    width: 2px; height: 92px;
    background: var(--text-soft);
  }
  .contact-list {
    position: absolute;
    left: 486px; top: 334px;
    margin: 0; padding: 0;
    list-style: none;
    color: var(--text-soft);
    font-size: 28px;
  }
  .contact-list li {
    display: flex;
    align-items: center;
    height: 37px;
  }
  .contact-list svg {
    width: 22px; height: 22px;
    margin-right: 12px;
    flex: none;
  }
</style>
</head>
<body>
<main class="canvas">

  <section class="card card--front" aria-label="Card front">
    <div class="brand-seal">
      <h1 class="brand-name">
        <span class="brand-name__main">BIRCH</span>
        <span class="brand-name__sub">FLOORING SUPPLY</span>
      </h1>
    </div>
  </section>

  <section class="card card--back" aria-label="Card back">
    <div class="pattern-band" role="img" aria-label="Grey and white geometric diamond lattice pattern"></div>
    <div class="gold-rule"></div>

    <div class="brand-seal">
      <p class="brand-name">
        <span class="brand-name__main">BIRCH</span>
        <span class="brand-name__sub">FLOORING SUPPLY</span>
      </p>
    </div>

    <div class="contact-person">
      <p class="contact-person__name">Dana Reyes</p>
      <p class="contact-person__role">DIRECTOR</p>
    </div>

    <div class="divider"></div>

    <ul class="contact-list">
      <li>
        <svg viewBox="0 0 24 24" aria-hidden="true"><path fill="#eee" d="M6.6 10.8a15.1 15.1 0 0 0 6.6 6.6l2.2-2.2c.3-.3.7-.4 1-.2 1.1.4 2.3.6 3.6.6.6 0 1 .4 1 1V20c0 .6-.4 1-1 1A17 17 0 0 1 3 4c0-.6.4-1 1-1h3.5c.6 0 1 .4 1 1 0 1.3.2 2.5.6 3.6.1.3 0 .7-.2 1z"/></svg>
        5550142876
      </li>
      <li>
        <svg viewBox="0 0 24 24" aria-hidden="true"><rect x="2" y="5" width="20" height="14" fill="none" stroke="#eee" stroke-width="2"/><path d="M2 5l10 8 10-8" fill="none" stroke="#eee" stroke-width="2"/></svg>
        hello@birchfloors.com
      </li>
      <li>
        <svg viewBox="0 0 24 24" aria-hidden="true"><circle cx="12" cy="12" r="10" fill="none" stroke="#eee" stroke-width="1.8"/><ellipse cx="12" cy="12" rx="4.5" ry="10" fill="none" stroke="#eee" stroke-width="1.5"/><path d="M2 12h20M4 7h16M4 17h16" stroke="#eee" stroke-width="1.5"/></svg>
        www.birchfloors.com
      </li>
    </ul>
  </section>

</main>
</body>
</html>
```